Business Card Design Project

We are an agricultural business based in Brisbane.
We design, manage and operate regional saleyards. Our logo is green/silver in colour and details of our business can be found on our website www.vodemarketyards.com.au

Just wanting a corporate design for some business cards and include name, position, contact details.

Thanks

Industry/Entity Type

Business

```html
<!DOCTYPE html>
<html lang="en">
<head>
<meta charset="utf-8">
<title>Vode Market Yards – Business Card</title>
<link rel="stylesheet" href="https://fonts.googleapis.com/css2?family=Roboto+Condensed:wght@400;700&display=swap">
<style>
  :root {
    --backdrop: #f1ece3;
    --card-front: #f6f6f6;
    --card-back: #e4e4e4;
    --band: #e2e2e2;
    --rail: #dadada;
    --ink: #2b2b2b;
    --ink-soft: #444;
    --green: #12903f;
    --ghost: #d6d6d6;
  }
  * { box-sizing: border-box; margin: 0; padding: 0; }
  html, body { width: 1200px; height: 900px; overflow: hidden; }
  body {
    background: var(--backdrop);
    font-family: "Roboto Condensed", "Arial Narrow", sans-serif;
    position: relative;
  }
  .card {
    position: absolute;
    top: 127px;
    width: 389px;
    height: 647px;
    box-shadow: 0 3px 8px rgba(0,0,0,.18);
    overflow: hidden;
  }
  .card--front { left: 135px; background: var(--card-front); }
  .card--back { left: 659px; background: var(--card-back); }

  .rail { position: absolute; left: 0; width: 43px; background: var(--rail); }
  .rail--top { top: 0; height: 396px; }
  .rail--bottom { top: 586px; height: 61px; }

  .name-band {
    position: absolute;
    left: 144px; top: 98px;
    width: 245px; height: 45px;
    background: var(--band);
    display: flex; align-items: center;
    padding-left: 7px;
  }
  .name {
    font-size: 31px; font-weight: 400; color: var(--ink);
    letter-spacing: -0.3px; white-space: nowrap;
  }
  .name .surname { color: var(--green); }
  .position {
    position: absolute; left: 151px; top: 149px;
    font-size: 13px; color: var(--ink-soft);
  }

  .ghost-name {
    position: absolute; left: 43px; right: 0; top: 258px;
    text-align: center;
    font-size: 34px; font-weight: 700; line-height: 1.05;
    color: var(--ghost); letter-spacing: 0.5px;
  }

  .contact { position: absolute; left: 0; top: 402px; list-style: none; }
  .contact-row {
    width: 345px; height: 39px; margin-bottom: 7px;
    background: var(--band);
    display: flex; align-items: center;
    font-size: 14px; color: var(--ink-soft);
  }
  .contact-icon { width: 14px; height: 14px; margin-left: 61px; margin-right: 9px; }
  .contact-text { margin-left: 84px; }
  .contact-icon + .contact-text { margin-left: 0; }

  .wordmark {
    position: absolute; left: 0; right: 0; top: 290px;
    display: flex; align-items: center; justify-content: center; gap: 12px;
  }
  .wordmark-mark { width: 18px; height: 18px; background: var(--green); }
  .wordmark-name {
    font-size: 34px; font-weight: 700; color: var(--ink);
    line-height: 1.05; letter-spacing: 0.5px;
  }
</style>
</head>
<body>
  <section class="card card--front" aria-label="Card front">
    <div class="rail rail--top"></div>
    <div class="rail rail--bottom"></div>

    <div class="name-band">
      <h1 class="name">Daniel <span class="surname">Hartley</span></h1>
    </div>
    <p class="position">General Manager</p>

    <p class="ghost-name" aria-hidden="true">VODE MARKET<br>YARDS</p>

    <ul class="contact">
      <li class="contact-row">
        <svg class="contact-icon" viewBox="0 0 14 14" aria-hidden="true">
          <path d="M7 0.5a4.5 4.5 0 0 0-4.5 4.5c0 3.3 4.5 8.5 4.5 8.5s4.5-5.2 4.5-8.5A4.5 4.5 0 0 0 7 0.5z" fill="var(--green)"/>
          <circle cx="7" cy="5" r="1.7" fill="var(--band)"/>
        </svg>
        <span class="contact-text">Your Street,</span>
      </li>
      <li class="contact-row"><span class="contact-text">Your City, Pincode</span></li>
      <li class="contact-row">
        <svg class="contact-icon" viewBox="0 0 14 14" aria-hidden="true">
          <path d="M5 1.5c-1 0-2.2 1-2.2 2.2 0 4.3 3.7 8.8 6.2 8.8 1.1 0 1.9-.8 2.1-1.6l-2-1.6-1.3.9C6.6 9.4 5.4 7.5 5 6l1.2-.9-.7-3.2z" fill="var(--green)"/>
        </svg>
        <span class="contact-text">0400 517 392</span>
      </li>
      <li class="contact-row">
        <svg class="contact-icon" viewBox="0 0 14 14" aria-hidden="true">
          <rect x="1" y="3" width="12" height="8.5" fill="none" stroke="var(--green)" stroke-width="1.4"/>
          <path d="M1 3.5l6 4.5 6-4.5" fill="none" stroke="var(--green)" stroke-width="1.4"/>
        </svg>
        <span class="contact-text">daniel@vodemarketyards.com.au</span>
      </li>
    </ul>
  </section>

  <section class="card card--back" aria-label="Card back">
    <div class="wordmark">
      <span class="wordmark-mark" aria-hidden="true"></span>
      <span class="wordmark-name">VODE MARKET YARDS</span>
    </div>
  </section>
</body>
</html>
```